1 page A4 double sided Brochure Design Folded to envelope size. Interesting fold design would be co

Small family run guesthouse BnB in Blue Mountains Australia needs a new brochure showing different aspects of business

We need a new brochure to go with our new website. Basically the design would be good as a double sided brochure that can be folded down to standard envelope size.

We have seen a few interesting brochure designs before that fold in different ways (and therefore have the design to match) but still fold down to this size to help with postage.

The design would have to showcase the different aspects of our business including individual accommodation for couples and families, conference market, wedding market, retreat market and events market (parties, re-unions etc). The Business must be Showcased as The Fernhollow Lodge, Blue Mountains

It is possible to arrange design so folds separate different sections of info/pictures.

It is also optional that we possibly have 2 brochures instead, one that is a basic all inclusive once described and one that only deals with group bookings (wedding conference retreats etc etc)

Must match design elements from our web page. Feel free to take informations, elements and images from there for design www.fernhollowlodge.com.au

Here is a link to our view we wake up to every morning to inspire all those working on a design!
http://www.fernhollowlodge.com.au/images/view.jpg

Target Market(s)

Group bookings, weddings, conferences, retreats, events and Blue Mountains Travellers

Industry/Entity Type

Accommodation

Requirements
Must have
• Must be based on our current websites design feel, colours, etc
Must be showcased as The Fernhollow Lodge Blue Mountains.
Must mention The Blue Mountains as a world heritage destination
Must be A4 double sided that can fold down to 1/3 the size to fit into a standard envelope. Any designs that will not fit in a standard envelope once folded can not be accepted as they are outside the brief
Nice to have
• Interesting folding design to get people interested to read it.

```html
<!DOCTYPE html>
<html lang="en">
<head>
<meta charset="utf-8">
<title>The Fernhollow Lodge Blue Mountains – Brochure Inside Spread</title>
<link href="https://fonts.googleapis.com/css2?family=Cinzel:wght@400&family=Questrial&display=swap" rel="stylesheet">
<style>
  :root {
    --stage: #ececec;
    --panel: #000000;
    --heading: #e6e6e6;
    --body-light: #d2d2d2;
    --body-dark: #1e2530;
    --room-warm: #b9a58c;
    --room-light: #e4ddd0;
    --mist-top: #b8bccb;
    --mist-bottom: #8f9fb6;
    --valley-top: #8ea2bb;
    --valley-bottom: #5f7f6a;
    --table-top: #3b4a47;
    --table-bottom: #2a2424;
    --cliff-green: #3f5a32;
    --cliff-rock: #9a6a3e;
    --overlay-dusk: rgba(38, 52, 88, 0.55);
  }
  * { box-sizing: border-box; margin: 0; padding: 0; }
  html, body {
    width: 1200px;
    height: 1000px;
    overflow: hidden;
    background: var(--stage);
  }
  .spread {
    position: absolute;
    left: 26px;
    top: 94px;
    width: 1150px;
    height: 813px;
    box-shadow: 0 0 24px rgba(0, 0, 0, 0.25);
    background: var(--panel);
  }
  .info-panel {
    position: absolute;
    left: 0;
    top: 0;
    width: 1150px;
    height: 406px;
    background: var(--panel);
    color: var(--body-light);
    font-family: "Questrial", "Century Gothic", sans-serif;
    font-size: 12px;
    line-height: 15.5px;
  }
  .column-intro {
    position: absolute;
    left: 39px;
    top: 36px;
    width: 330px;
  }
  .column-groups {
    position: absolute;
    left: 407px;
    top: 36px;
    width: 712px;
  }
  .section-title {
    font-family: "Cinzel", "Trajan Pro", serif;
    font-weight: 400;
    font-size: 14px;
    letter-spacing: 2.6px;
    color: var(--heading);
    margin-bottom: 10px;
  }
  .info-panel p { margin-bottom: 10px; }
  .section-title.weddings { margin-top: 30px; }

  .photo-grid {
    position: absolute;
    left: 0;
    top: 406px;
    width: 1150px;
    height: 407px;
  }
  .tile {
    position: absolute;
    display: flex;
    align-items: center;
    justify-content: center;
    text-align: center;
    font-family: "Questrial", "Century Gothic", sans-serif;
    font-size: 12px;
    line-height: 15.5px;
  }
  .tile-room {
    left: 0; top: 0; width: 387px; height: 193px;
    background: linear-gradient(100deg, #8a5a44 0%, var(--room-warm) 22%, var(--room-light) 55%, #cfc4b4 100%);
  }
  .tile-mist {
    left: 387px; top: 0; width: 387px; height: 193px;
    background: linear-gradient(180deg, var(--mist-top) 0%, #a9b1c4 50%, var(--mist-bottom) 100%);
    color: var(--body-dark);
  }
  .tile-mist .caption { width: 300px; margin-top: -30px; }
  .tile-cliff {
    left: 774px; top: 0; width: 376px; height: 407px;
    background:
      linear-gradient(180deg, #6f7f96 0%, #5c6f6a 30%, transparent 48%),
      linear-gradient(90deg, #6f8aa6 0%, #6a8a74 30%, var(--cliff-rock) 48%, #7a5a34 62%, var(--cliff-green) 80%, #2f4726 100%);
  }
  .tile-cliff .dusk {
    position: absolute;
    left: 0; top: 0; width: 376px; height: 193px;
    background: var(--overlay-dusk);
    display: flex;
    align-items: center;
    justify-content: center;
    color: #e8ecf2;
  }
  .tile-cliff .caption { width: 215px; margin-top: -30px; }
  .tile-valley {
    left: 0; top: 193px; width: 387px; height: 214px;
    background: linear-gradient(180deg, var(--valley-top) 0%, #7d96a8 45%, var(--valley-bottom) 100%);
    color: var(--body-dark);
  }
  .tile-valley .caption { width: 245px; margin-top: -30px; }
  .tile-table {
    left: 387px; top: 193px; width: 387px; height: 214px;
    background: linear-gradient(180deg, #5d7565 0%, var(--table-top) 35%, #4a3a38 65%, var(--table-bottom) 100%);
  }
</style>
</head>
<body>
  <main class="spread">
    <section class="info-panel">
      <div class="column-intro">
        <h2 class="section-title">So Close…Yet Worlds Away</h2>
        <p>The Fernhollow Lodge Blue Mountains is a small family run guesthouse, bush retreat and function centre.</p>
        <p>Located on 32 acres of pristine virgin bushland in the centre of world heritage listed national park land The Fernhollow Lodge is your perfect Blue Mountains accommodation whether you are looking for a quiet place to escape with someone special or a function or conference venue in the Blue Mountains for your next group escape or private, personal, specially tailored wedding.</p>
        <p>The Fernhollow Lodge has 2 buildings. The main retreat with 20 well appointed en suited rooms, each with views across the pool and valley, along with 2 function rooms, games room, commercial kitchen, pool and outdoor BBQ area.</p>
        <p>The second is our manor house, a large, simple 7 bedroom, 4 bathroom house with lounge kitchen and dining room.</p>
      </div>
      <div class="column-groups">
        <h2 class="section-title">Conferences, Retreats and Special Events</h2>
        <p>The Fernhollow Lodge prides itself as the venue of choice for many of the worlds best companies for their conference needs.</p>
        <p>Between our main retreat, the manor house and Ridgeview Cottage we have various configurations available for any style or number for your next Blue Mountains conference from 4 attendees up to 50</p>
        <p>Our main function/conference room is suitable for up to 25 people in Ushape, 30 People in Classroom style or 80 people banquet style. It is modern and stylish with high ceilings, Large wooden tables, and views outside to bush trees.</p>
        <h2 class="section-title weddings">Weddings</h2>
        <p>At The Fernhollow Lodge you can have your ceremony, reception and accommodation for all your guests for the price you normally pay for one and get all 3.&nbsp; With accommodation for up to 70 people we can help you plan your wedding your way.&nbsp; Whether its a cocktail style wedding for 150 people, a formal sit down reception for 70, or a quiet, casual picnic basket event for 40 we have seen it all at The Fernhollow Lodge.</p>
      </div>
    </section>

    <section class="photo-grid">
      <div class="tile tile-room" role="img" aria-label="Guest bedroom with made bed, towels and French doors opening to the garden"></div>
      <div class="tile tile-mist" role="img" aria-label="Misty Blue Mountains valley view">
        <p class="caption">The Fernhollow Lodge is a very special, personal, peacful choice for your Blue Mountains accommodation. Being Located on 32 acres of mostly virgin bushland, including endangered hanging swamp, backing onto national parkland, The Fernhollow Lodge allows you to experience the Blue Mountains in its true splendour.</p>
      </div>
      <div class="tile tile-cliff" role="img" aria-label="Sandstone cliff face covered in green bushland above the valley">
        <div class="dusk">
          <p class="caption">A true retreat requires something special to really let go of the outside world and focus on that which is truely important.</p>
        </div>
      </div>
      <div class="tile tile-valley" role="img" aria-label="Forested valley seen from a sandstone cliff edge">
        <p class="caption">Together with our private, friendly, family run atmosphere The Fernhollow Lodge is the perfect place to escape the real world and explore another.</p>
      </div>
      <div class="tile tile-table" role="img" aria-label="Outdoor dining table set with wine glasses and red napkins overlooking the bush"></div>
    </section>
  </main>
</body>
</html>
```